Business Card Design Project

I want a cleaner business card and envelope then what we have now, its too crowded.
Updates

I update with logo, this can be changed anyway you feel it looks best. I also have put gaurantee on there and extended time, this is my first time doing this. Also gave an example of current card

Target Market(s)

a wide array of customers from lattice 700 to small companies and cleints

Industry/Entity Type

Business

Requirements
Must have
• Need to have address, telephone number email
Nice to have
• a sharp professional card that stands out but is still very clean.
Should not have
• Not crazy looking

```html
<!DOCTYPE html>
<html lang="en">
<head>
<meta charset="utf-8">
<title>Halvard Insurance Group – Stationery</title>
<link rel="stylesheet" href="https://fonts.googleapis.com/css2?family=Montserrat:wght@500&family=Arimo:wght@400;700&family=Open+Sans:wght@400&display=swap">
<style>
  :root {
    --stage-dark: #141414;
    --stage-mid: #262626;
    --label: #ffffff;
    --paper: #ffffff;
    --silver-light: #e6e8e8;
    --silver-mid: #b3b8b7;
    --silver-dark: #7d8584;
    --ink: #2b2f2f;
    --ink-soft: #7a8281;
  }
  * { margin: 0; padding: 0; box-sizing: border-box; }
  html, body { width: 1200px; height: 900px; overflow: hidden; }
  body {
    position: relative;
    background: linear-gradient(90deg, var(--stage-dark), var(--stage-mid) 30%, var(--stage-dark) 55%, var(--stage-mid) 80%, var(--stage-dark));
    font-family: "Arimo", Arial, sans-serif;
  }
  .piece-label {
    position: absolute;
    transform: translateX(-50%);
    color: var(--label);
    font-family: "Open Sans", Arial, sans-serif;
    font-size: 30px;
    white-space: nowrap;
  }
  .piece { position: absolute; overflow: hidden; }
  .piece svg.swoosh { position: absolute; left: 0; top: 0; width: 100%; height: 100%; }
  .brand { position: absolute; text-align: center; }
  .brand-mark {
    display: block;
    margin: 0 auto;
    background: linear-gradient(135deg, var(--silver-light), var(--silver-dark));
  }
  .brand-name {
    display: block;
    font-family: "Montserrat", Arial, sans-serif;
    font-weight: 500;
    color: var(--ink);
    line-height: 1.1;
  }
  .brand-name .line-sub { display: block; }

  /* Business card front */
  .card-front {
    left: 35px; top: 135px; width: 522px; height: 290px; border-radius: 12px;
    background: radial-gradient(ellipse at 50% 40%, var(--silver-light) 0%, var(--silver-mid) 60%, var(--silver-dark) 100%);
  }
  .card-front .brand { left: 0; right: 0; top: 64px; }
  .card-front .brand-mark { width: 76px; height: 76px; margin-bottom: 18px; }
  .card-front .brand-name { font-size: 33px; letter-spacing: 3px; }
  .card-front .brand-name .line-sub { font-size: 15px; letter-spacing: 3px; margin-top: 4px; }
  .card-front .web {
    position: absolute; left: 0; right: 0; top: 263px; text-align: center;
    color: var(--paper); font-size: 14px;
  }

  /* Business card back */
  .card-back {
    left: 35px; top: 524px; width: 525px; height: 291px; border-radius: 12px;
    background: var(--paper);
  }
  .card-back .brand { left: 22px; width: 210px; top: 22px; }
  .card-back .brand-mark { width: 77px; height: 77px; margin-bottom: 14px; }
  .card-back .brand-name { font-size: 28px; letter-spacing: 2px; }
  .card-back .brand-name .line-sub { font-size: 14px; letter-spacing: 2px; margin-top: 3px; }
  .contact {
    position: absolute; right: 14px; text-align: right;
    font-size: 13px; color: var(--ink); line-height: 1.15;
  }
  .contact-person { top: 10px; }
  .contact-person .role { color: var(--ink-soft); }
  .contact-details { top: 170px; }
  .contact-details .address { margin-bottom: 14px; }
  .contact-details b { font-weight: 700; }

  /* Envelope back */
  .envelope-back {
    left: 604px; top: 131px; width: 557px; height: 305px; background: var(--paper);
  }
  .envelope-back .brand { left: 0; right: 0; top: 12px; }
  .envelope-back .brand-mark { width: 46px; height: 44px; margin-bottom: 8px; }
  .envelope-back .brand-name { font-size: 19px; letter-spacing: 2px; }
  .envelope-back .brand-name .line-sub { font-size: 9px; letter-spacing: 1.5px; margin-top: 1px; }

  /* Envelope front */
  .envelope-front {
    left: 606px; top: 497px; width: 552px; height: 318px; background: var(--paper);
  }
  .envelope-front .brand { left: 14px; width: 126px; top: 28px; }
  .envelope-front .brand-mark { width: 46px; height: 46px; margin-bottom: 8px; }
  .envelope-front .brand-name { font-size: 19px; letter-spacing: 2px; }
  .envelope-front .brand-name .line-sub { font-size: 9px; letter-spacing: 1.5px; margin-top: 1px; }
  .return-address {
    position: absolute; left: 16px; top: 120px;
    font-size: 9px; line-height: 1.3; color: var(--ink);
  }
  .return-address span { display: block; }
  .return-address .street { padding-left: 10px; }
</style>
</head>
<body>

<div class="piece-label" style="left:308px; top:82px;">Business Card Front</div>
<div class="piece-label" style="left:828px; top:82px;">Envelope Back</div>
<div class="piece-label" style="left:296px; top:466px;">Business Card Back</div>
<div class="piece-label" style="left:884px; top:448px;">Envelope Front</div>

<section class="piece card-front">
  <div class="brand">
    <span class="brand-mark"></span>
    <span class="brand-name">HALVARD<span class="line-sub">INSURANCE GROUP</span></span>
  </div>
  <div class="web">www.halvardagency.com</div>
</section>

<section class="piece card-back">
  <svg class="swoosh" viewBox="0 0 525 291" preserveAspectRatio="none" aria-hidden="true">
    <defs>
      <linearGradient id="cardBand" x1="0" y1="0" x2="1" y2="0">
        <stop offset="0" stop-color="#7d8584"/>
        <stop offset="0.45" stop-color="#e6e8e8"/>
        <stop offset="1" stop-color="#9aa1a0"/>
      </linearGradient>
    </defs>
    <path d="M0,185 C120,200 230,118 340,128 C430,136 490,150 525,175 L525,291 L0,291 Z" fill="url(#cardBand)"/>
    <path d="M0,195 C120,212 230,132 340,142 C430,150 490,164 525,188" fill="none" stroke="#ffffff" stroke-width="3" opacity="0.7"/>
  </svg>
  <div class="brand">
    <span class="brand-mark"></span>
    <span class="brand-name">HALVARD<span class="line-sub">INSURANCE GROUP</span></span>
  </div>
  <div class="contact contact-person">
    <div>Maren Olsted-Price</div>
    <div class="role">Operations Manager</div>
  </div>
  <div class="contact contact-details">
    <div class="address">18230 Corwin Ave,<br>Ashford Hills, MI 48021</div>
    <div><b>Phone:</b> 555-214-3800</div>
    <div><b>Ext:</b> 323</div>
    <div><b>Direct:</b>555-214-0192</div>
    <div><b>Fax:</b>555-214-3803</div>
    <div style="margin-top:3px;">molsted-price@halvardagency.com</div>
  </div>
</section>

<section class="piece envelope-back">
  <svg class="swoosh" viewBox="0 0 557 305" preserveAspectRatio="none" aria-hidden="true">
    <defs>
      <linearGradient id="flapFill" x1="0" y1="0" x2="1" y2="0">
        <stop offset="0" stop-color="#8d9594"/>
        <stop offset="0.5" stop-color="#f2f3f3"/>
        <stop offset="1" stop-color="#8d9594"/>
      </linearGradient>
    </defs>
    <path d="M0,0 L557,0 L557,8 Q545,28 505,42 L300,104 Q278,112 256,104 L52,42 Q12,28 0,8 Z" fill="url(#flapFill)"/>
  </svg>
  <div class="brand">
    <span class="brand-mark"></span>
    <span class="brand-name">HALVARD<span class="line-sub">INSURANCE GROUP</span></span>
  </div>
</section>

<section class="piece envelope-front">
  <svg class="swoosh" viewBox="0 0 552 318" preserveAspectRatio="none" aria-hidden="true">
    <defs>
      <linearGradient id="envBand" x1="0" y1="0" x2="1" y2="0">
        <stop offset="0" stop-color="#7d8584"/>
        <stop offset="0.5" stop-color="#e6e8e8"/>
        <stop offset="1" stop-color="#8d9594"/>
      </linearGradient>
    </defs>
    <path d="M0,296 C150,290 340,250 460,256 C515,259 540,270 552,282 L552,318 L0,318 Z" fill="url(#envBand)"/>
    <path d="M0,302 C150,297 340,258 460,264 C515,267 540,278 552,290" fill="none" stroke="#ffffff" stroke-width="2" opacity="0.7"/>
  </svg>
  <div class="brand">
    <span class="brand-mark"></span>
    <span class="brand-name">HALVARD<span class="line-sub">INSURANCE GROUP</span></span>
  </div>
  <div class="return-address">
    <span class="street">18230 Corwin Ave.</span>
    <span>Ashford Hills, MI 48021</span>
  </div>
</section>

</body>
</html>
```